Real Estate Marketing Company Needs 1 Page 8.5x11 Price List Flyer Design

We need a 1 page 8.5in x 11in price list flyer that is intended for drop off at local offices. This is intended to show all the services we offer including pricing to potential new clients. It should be separated into sections for the different services we offer. I'd also like some photos and our Logo on the list to make it look nice so its not all text. Try to incorporate the logo colors in the design.

Industry/Entity Type

Real Estate

Requirements
Must have
• Price List
• Photos
• Logo
• website address

```html
<!DOCTYPE html>
<html lang="en">
<head>
<meta charset="utf-8">
<title>Open Gate Photography – Price List</title>
<link href="https://fonts.googleapis.com/css2?family=Big+Shoulders+Display:wght@200&family=Open+Sans:wght@400;600;700&family=Cinzel:wght@500&display=swap" rel="stylesheet">
<style>
  :root {
    --backdrop: #8a8a88;
    --paper: #ffffff;
    --ink: #1d1d1d;
    --ink-soft: #3a3a3a;
    --frame: #b9b9b9;
    --headline-grey: #8c8c8c;
    --bar-grey: #c6c6c6;
    --brand-red: #b3262a;
    --dash: #8f8f8f;
  }
  * { box-sizing: border-box; margin: 0; padding: 0; }
  html, body { width: 1200px; height: 802px; overflow: hidden; }
  body { background: var(--backdrop); font-family: "Open Sans", Arial, sans-serif; color: var(--ink); position: relative; }

  .page { position: absolute; top: 70px; width: 522px; height: 670px; background: var(--paper); }
  .page--cover { left: 70px; }
  .page--prices { left: 608px; }

  /* Cover */
  .cover-frame { position: absolute; left: 22px; top: 22px; width: 477px; height: 626px; border: 1px solid var(--frame); }
  .tagline-small { position: absolute; left: 97px; top: 134px; font-family: "Big Shoulders Display", "Arial Narrow", sans-serif; font-weight: 200; font-size: 24px; letter-spacing: 1.5px; color: var(--ink-soft); }
  .tagline-large { position: absolute; left: 95px; top: 160px; font-family: "Big Shoulders Display", "Arial Narrow", sans-serif; font-weight: 200; font-size: 58px; line-height: 1; letter-spacing: 1px; color: var(--headline-grey); }
  .hero-photo { position: absolute; left: 22px; top: 230px; width: 477px; height: 246px; background: linear-gradient(180deg, #3f6b2d 0%, #4f7c38 45%, #3aa0c4 72%, #6aa14a 100%); }
  .accent-bar { position: absolute; left: 50px; top: 477px; width: 422px; height: 6px; background: var(--bar-grey); }
  .circle-photo { position: absolute; border-radius: 50%; border: 8px solid var(--paper); }
  .circle-photo--porch { left: 323px; top: 118px; width: 152px; height: 152px; background: linear-gradient(160deg, #6a9a3a 0%, #c9c3b4 55%, #c8612f 75%, #8a8378 100%); }
  .circle-photo--house { left: 81px; top: 404px; width: 152px; height: 152px; background: linear-gradient(180deg, #b98fc4 0%, #7a4c6a 45%, #5a3b3a 70%, #e9e6f2 100%); }
  .brand { position: absolute; left: 327px; top: 524px; width: 160px; text-align: center; }
  .brand-mark { display: block; margin: 0 auto 8px; }
  .brand-name { font-family: "Cinzel", Georgia, serif; font-weight: 500; font-size: 17px; letter-spacing: 1px; color: var(--ink); line-height: 1.1; }
  .brand-sub { font-family: "Cinzel", Georgia, serif; font-weight: 500; font-size: 7px; letter-spacing: 6px; color: var(--ink); margin-top: 3px; }

  /* Price page */
  .abs { position: absolute; }
  .section-title { font-weight: 700; font-size: 14px; letter-spacing: .2px; color: var(--ink); }
  .body-text { font-size: 9.6px; line-height: 1.35; color: var(--ink-soft); }
  .fine { font-size: 7.2px; color: var(--ink-soft); }
  .price-col { position: absolute; top: 79px; width: 130px; }
  .price-col h3 { font-size: 12px; font-weight: 700; margin-bottom: 3px; }
  .price-col .price { font-size: 14px; font-weight: 700; color: var(--ink); margin-top: 2px; }
  .vdivider { position: absolute; top: 74px; height: 72px; border-left: 1px dashed var(--dash); }
  .hdivider { position: absolute; height: 0; border-top: 1px dashed var(--dash); }
  .bundles { left: 53px; top: 195px; font-size: 9px; color: var(--ink-soft); }
  .bundles b { color: var(--ink); }
  .bundles .sep { margin: 0 9px; }
  .interior-photo { left: 54px; top: 240px; width: 242px; height: 157px; background: linear-gradient(180deg, #c7b79f 0%, #b5a48a 40%, #8f7f6a 70%, #5e5448 100%); }
  .services { left: 317px; top: 239px; width: 200px; }
  .services .section-title { margin-bottom: 8px; }
  .services p { margin-bottom: 10px; }
  .services b, .floor b { color: var(--ink); font-weight: 700; }
  .plan-drawing { left: 53px; top: 431px; width: 158px; height: 202px; background: linear-gradient(180deg, #f2f2f2, #e4e4e4); border: 1px solid #cfcfcf; }
  .floor { left: 247px; top: 446px; width: 240px; }
  .floor .section-title { margin-bottom: 6px; }
  .floor p.body-text { margin-bottom: 8px; }
  .contact { left: 248px; top: 580px; font-size: 10.2px; line-height: 1.38; color: var(--ink-soft); }
  .contact b { color: var(--ink); }
</style>
</head>
<body>

<section class="page page--cover">
  <div class="cover-frame"></div>
  <div class="tagline-small">PRESENTATION IS</div>
  <div class="tagline-large">EVERYTHING</div>
  <div class="hero-photo" role="img" aria-label="Backyard with landscaped garden, swimming pool and white pool house"></div>
  <div class="accent-bar"></div>
  <div class="circle-photo circle-photo--porch" role="img" aria-label="Covered porch with cushioned bench and rocking chairs"></div>
  <div class="circle-photo circle-photo--house" role="img" aria-label="Brick colonial house at dusk in winter snow"></div>
  <div class="brand">
    <svg class="brand-mark" width="56" height="56" viewBox="0 0 56 56" aria-hidden="true">
      <circle cx="28" cy="28" r="26" fill="none" stroke="var(--ink)" stroke-width="3"/>
    </svg>
    <div class="brand-name">OPEN GATE</div>
    <div class="brand-sub">PHOTOGRAPHY</div>
  </div>
</section>

<section class="page page--prices">
  <h2 class="abs section-title" style="left:53px;top:48px;">PACKAGE PRICING:</h2>

  <div class="price-col" style="left:53px;">
    <h3>Silver Package:</h3>
    <div class="body-text">15 Photos +<br>Floor Plan (3,500 sqft)</div>
    <div class="price">$225</div>
  </div>
  <div class="vdivider" style="left:175px;"></div>
  <div class="price-col" style="left:196px;">
    <h3>Gold Package:</h3>
    <div class="body-text">25 Photos +<br>Floor Plan (4,500 sqft)</div>
    <div class="price">$300</div>
  </div>
  <div class="vdivider" style="left:318px;"></div>
  <div class="price-col" style="left:340px;">
    <h3>Platinum Package:</h3>
    <div class="body-text">35 Photos +<br>Floor Plan (5,500 sqft)</div>
    <div class="price">$375</div>
  </div>

  <div class="hdivider" style="left:53px;top:164px;width:423px;"></div>

  <h2 class="abs section-title" style="left:53px;top:176px;">PHOTOGRAPHY ONLY</h2>
  <div class="abs bundles">15 Photo Bundle : <b>$100</b><span class="sep">|</span>25 Photo Bundle : <b>$150</b><span class="sep">|</span>35 Photo Bundle : <b>$200</b></div>

  <div class="hdivider" style="left:50px;top:223px;width:422px;"></div>

  <div class="abs interior-photo" role="img" aria-label="Bright living room with high ceiling, arched windows and lanterns"></div>
  <div class="abs services">
    <h2 class="section-title">ADDITIONAL SERVICES</h2>
    <p class="body-text">Aerial Photos: 3-6 Photos - <b>$200</b><br><span class="fine">($75 if combined with another package)</span></p>
    <p class="body-text">Aerial Video: (1-3 min video) - <b>$375</b></p>
    <p class="body-text">Branded Video Tour w/ Aerial Video:<br>(2-4 min video of property) - <b>$800-$1300</b><br><span class="fine">(voiceover optional, call for details)</span></p>
    <p class="body-text" style="margin-bottom:0;">Twilight Photos: 3-6 Photos - <b>$225</b><br>Luxury Package: <b>$2,000</b><br><span class="fine">(includes all services listed)</span></p>
  </div>

  <div class="hdivider" style="left:50px;top:414px;width:422px;"></div>

  <div class="abs plan-drawing" role="img" aria-label="Two-storey house floor plan drawing with labelled rooms"></div>
  <div class="abs floor">
    <h2 class="section-title">FLOOR PLANS</h2>
    <p class="body-text">Floor Plan (3,500 sqft) - <b>$150</b></p>
    <p class="body-text">Floor Plan (4,500 sqft) - <b>$175</b></p>
    <p class="body-text">Floor Plan (5,500 sqft) - <b>$200</b></p>
    <div class="fine">*$25 per additional 500sqft<br>**Complex floor plans are priced individually regardless of sqft</div>
  </div>

  <div class="hdivider" style="left:248px;top:562px;width:236px;"></div>

  <div class="abs contact">
    For more information or to book<br>
    a shoot please visit our website:<br>
    <b>www.OpenGatePhotography.com</b> or<br>
    call Dana at <b>555-014-2280</b>
  </div>
</section>

</body>
</html>
```